Simple Website Design for Law Office

I need a website design for our law office (Law Offices of Marcus Trell) that is extremely simple, only including a landing page and perhaps a contact page (parallax scrolling).

Website should look similar to this one (template): https://www.quorvelbaxon.com/

Design should be modern, simple, and inviting. There are a few assets like logo, stock photos/icons we would like added as well, and some language and contact info, but very basic stuff.

The name of the company is: Law Offices of Marcus Trell

Target Market(s)

B2B corporate clients, users from Canada, UK, East Asia, and all potential users with immigration needs

Coding

Coded - Design and coding required

Number of Pages Required

2 page

Colors

Designer to choose colors to be used in the design.

Requirements
Must have
• Landing page, Contact Page
• Simple, elegant design with minimalist font
Nice to have
• Parallax scrolling, so one page and can scroll to contact us segment

```html
<!DOCTYPE html>
<html lang="en">
<head>
<meta charset="utf-8">
<title>Law Offices of Marcus Trell</title>
<link rel="stylesheet" href="https://fonts.googleapis.com/css2?family=Tinos&family=Open+Sans:wght@300;400;600;700&family=Lato:wght@400;700&display=swap">
<style>
:root{
  --navy:#1b1a45;
  --navy-soft:#2b2a5a;
  --frame:#7d7ea0;
  --ink:#1d1c3e;
  --paper:#ffffff;
  --mist:#f3f3f3;
  --night:#2e3038;
  --footer:#27282d;
  --muted:#c9ccd4;
}
*{margin:0;padding:0;box-sizing:border-box}
html,body{width:1200px;height:2322px;overflow:hidden}
body{position:relative;background:var(--paper);font-family:"Open Sans",sans-serif;color:var(--ink)}
.abs{position:absolute}

/* hero */
.hero{position:absolute;left:0;top:0;width:1200px;height:642px;
  background:linear-gradient(180deg,#3b3f47 0%,#414a52 25%,#3d4c55 40%,#48533e 60%,#3f4a30 80%,#3a3f34 100%)}
.nav a{position:absolute;top:53px;font-family:"Open Sans",sans-serif;font-weight:600;font-size:13px;letter-spacing:.3px;color:#c8cad0;text-decoration:none}
.nav a.active{color:#fff}
.nav a.active::after{content:"";position:absolute;left:0;right:-2px;top:24px;height:2px;background:#fff}
.brand-box{position:absolute;left:511px;top:17px;width:178px;height:88px;border:2px solid #9a9ca4;
  display:flex;align-items:center;justify-content:center;font-family:"Tinos",serif;font-size:25px;color:#fff;letter-spacing:.5px}
.hero-title{position:absolute;left:0;width:1200px;top:246px;text-align:center;font-family:"Tinos",serif;font-size:60px;color:#fff;letter-spacing:1px}
.hero-sub{position:absolute;left:0;width:1200px;top:316px;text-align:center;font-weight:300;font-size:20px;letter-spacing:1.5px;color:#fff}
.btn-solid{position:absolute;background:var(--navy);color:#fff;font-weight:600;display:flex;align-items:center;justify-content:center;text-decoration:none}
.hero .btn-solid{left:471px;top:371px;width:258px;height:46px;font-size:13px;letter-spacing:.2px}
.dots{position:absolute;left:572px;top:597px;display:flex;gap:7px}
.dots span{width:9px;height:9px;border-radius:50%;background:#fff}
.dots span.on{background:transparent;border:1.5px solid #9fd08a}

/* success */
.section-title{position:absolute;left:0;width:1200px;text-align:center;font-family:"Tinos",serif;font-size:37px;color:var(--navy);letter-spacing:.5px}
.card{position:absolute;top:843px;width:272px;height:258px;border:2px solid var(--frame)}
.card-icon{position:absolute;left:79px;top:-57px;width:114px;height:114px;border-radius:50%;background:var(--navy);border:3px solid #8d8eab}
.card-icon svg{width:100%;height:100%}
.card h3{position:absolute;left:0;width:100%;top:78px;text-align:center;font-family:"Open Sans",sans-serif;font-weight:600;font-size:14.5px;color:var(--navy)}
.card p{position:absolute;left:20px;right:20px;top:106px;text-align:center;font-family:"Lato",sans-serif;font-size:13px;line-height:21.6px;color:#1e1e2a}
.btn-outline{position:absolute;left:71px;top:234px;width:128px;height:44px;background:#fff;border:2px solid var(--frame);
  display:flex;align-items:center;justify-content:center;font-weight:600;font-size:13.5px;color:var(--navy)}

/* about */
.about{position:absolute;left:0;top:1215px;width:1200px;height:487px;background:var(--mist)}
.about h4{position:absolute;left:143px;top:186px;font-weight:600;font-size:23.5px;color:var(--navy)}
.about .role{position:absolute;left:145px;top:228px;font-weight:300;font-size:25px;color:#222}
.about p{position:absolute;left:144px;top:272px;width:600px;font-size:15.3px;line-height:23px;color:#1d1c3e}
.about .btn-solid{left:144px;top:359px;width:126px;height:42px;font-size:14.5px;font-weight:400}
.portrait{position:absolute;left:841px;top:170px;width:213px;height:242px;border:4px solid #9c9db0;
  background:radial-gradient(circle at 50% 40%,#b8a89a 0%,#8b8a8a 40%,#5b6b7a 75%,#3f4f5e 100%)}

/* contact */
.contact{position:absolute;left:0;top:1702px;width:1200px;height:539px;
  background:linear-gradient(180deg,#33353d 0%,#2d3038 60%,#3a3532 100%)}
.contact h2{position:absolute;left:144px;top:66px;font-family:"Tinos",serif;font-weight:400;font-size:37px;line-height:44px;color:#fff;letter-spacing:.5px}
.info{position:absolute;left:144px;color:#fff;font-size:15px;line-height:21.6px;display:flex;gap:8px}
.info svg{flex:none;margin-top:3px}
.map{position:absolute;left:438px;top:68px;width:562px;height:300px;border:5px solid #8a8b91;
  background:linear-gradient(135deg,#e9e9ea 0%,#dfe1e4 50%,#e6e4de 100%)}

/* footer */
.footer{position:absolute;left:0;top:2241px;width:1200px;height:81px;background:var(--footer)}
.footer small{position:absolute;top:32px;font-size:11.5px;color:var(--muted)}
.social{position:absolute;left:906px;top:21px;display:flex;gap:3px}
.social span{width:37px;height:37px;border-radius:50%;background:var(--navy-soft);border:2px solid #9a9db0}
</style>
</head>
<body>

<header class="hero" role="img" aria-label="Aerial photo of a lakeside city skyline with parkland">
  <nav class="nav">
    <a class="active" href="#home" style="left:282px">HOME</a>
    <a href="#success" style="left:369px">OUR SUCCESS</a>
    <a href="#about" style="left:737px">MARCUS TRELL</a>
    <a href="#contact" style="left:855px">CONTACT</a>
  </nav>
  <div class="brand-box">MARCUS TRELL</div>
  <h1 class="hero-title">MARCUS TRELL</h1>
  <div class="hero-sub">Law Offices of Marcus Trell</div>
  <a class="btn-solid" href="#contact">CONTACT US FOR A CONSULTATION</a>
  <div class="dots"><span class="on"></span><span></span><span></span><span></span></div>
</header>

<section id="success">
  <h2 class="section-title" style="top:695px">OUR SUCCESS</h2>

  <div class="card" style="left:144px">
    <div class="card-icon">
      <svg viewBox="0 0 108 108" fill="none" stroke="#fff" stroke-width="2.4" stroke-linejoin="round" stroke-linecap="round">
        <rect x="50" y="28" width="26" height="16" transform="rotate(45 63 36)"/>
        <line x1="55" y1="52" x2="32" y2="78"/>
        <line x1="60" y1="56" x2="36" y2="82"/>
        <line x1="32" y1="78" x2="36" y2="82"/>
      </svg>
    </div>
    <h3>FORECLOSURE / HBOR</h3>
    <p>$1,880,000 settlement for loan servicer’s wrongful foreclosure, wrongful eviction, conversion, and reckless mishandling of loan modification.</p>
    <div class="btn-outline">LEARN MORE</div>
  </div>

  <div class="card" style="left:464px">
    <div class="card-icon">
      <svg viewBox="0 0 108 108" fill="none" stroke="#fff" stroke-width="2.2" stroke-linecap="round" stroke-linejoin="round">
        <circle cx="58" cy="44" r="8"/>
        <path d="M46 82V60c0-5 5-8 12-8s12 3 12 8v22M52 68v14M64 68v14"/>
        <path d="M40 58l-4 6 4 4M66 30l3-4M72 34l4-2M62 28l0-4"/>
      </svg>
    </div>
    <h3>PERSONAL INJURY / INSURANCE</h3>
    <p>$100,000 for damage to commercial property after carrier’s initial denial to extend coverage under client’s policy. $75,000 settlement for violent.</p>
    <div class="btn-outline">LEARN MORE</div>
  </div>

  <div class="card" style="left:784px">
    <div class="card-icon">
      <svg viewBox="0 0 108 108" fill="none" stroke="#fff" stroke-width="2.2">
        <circle cx="42" cy="66" r="12"/><circle cx="42" cy="66" r="8"/>
        <circle cx="66" cy="46" r="12"/><circle cx="66" cy="46" r="8"/>
        <path d="M46 54l6-10M54 40l4-4"/>
      </svg>
    </div>
    <h3>CRIMINAL</h3>
    <p>Domestic violence charges dismissed prior to jury selection. Drug sales charges referred to drug court and charges expunged.</p>
    <div class="btn-outline">LEARN MORE</div>
  </div>
</section>

<section id="about" class="about">
  <h2 class="section-title" style="top:63px">MARCUS TRELL</h2>
  <h4>LAW OFFICES OF MARCUS TRELL</h4>
  <div class="role">Attorney</div>
  <p>Handle all clients needs including criminal, transactional, and general civil litigation: personal injury, wrongful foreclosure/loan modification, breach of contract.</p>
  <a class="btn-solid" href="#about">LEARN MORE</a>
  <div class="portrait" role="img" aria-label="Portrait photo of the attorney"></div>
</section>

<section id="contact" class="contact" role="img" aria-label="Dim background photo of a city skyline at dusk">
  <h2>CONTACT<br>ADDRESS</h2>
  <div class="info" style="top:180px">
    <svg width="12" height="16" viewBox="0 0 12 16"><path d="M6 0a6 6 0 0 0-6 6c0 4.5 6 10 6 10s6-5.5 6-10a6 6 0 0 0-6-6zm0 8.5A2.5 2.5 0 1 1 6 3.5a2.5 2.5 0 0 1 0 5z" fill="#fff"/></svg>
    <div>Law Offices of Marcus Trell<br>2210 Harlow Ave., 4th Floor<br>Corran Vale, CA 90417</div>
  </div>
  <div class="info" style="top:261px">
    <svg width="14" height="11" viewBox="0 0 14 11"><rect width="14" height="11" rx="1" fill="#fff"/><path d="M0.5 1l6.5 5 6.5-5" stroke="#2e3038" stroke-width="1.3" fill="none"/></svg>
    <div>mtrelllaw@postvale.com</div>
  </div>
  <div class="info" style="top:301px">
    <svg width="14" height="14" viewBox="0 0 14 14"><path d="M3 0l2.5 3.5-1.5 2c1 2 2.5 3.5 4.5 4.5l2-1.5L14 11l-1.5 3C6 13.5.5 8 0 1.5z" fill="#fff"/></svg>
    <div>Tel: (555) 214-3077</div>
  </div>
  <div class="info" style="top:341px">
    <svg width="14" height="14" viewBox="0 0 14 14"><rect x="0" y="4" width="14" height="10" rx="1" fill="#fff"/><rect x="3" y="0" width="8" height="5" fill="#fff"/><rect x="3" y="7" width="8" height="1.5" fill="#2e3038"/><rect x="3" y="10" width="8" height="1.5" fill="#2e3038"/></svg>
    <div>Fax: (555) 214-3078</div>
  </div>
  <div class="map" role="img" aria-label="Street map showing the office location"></div>
</section>

<footer class="footer">
  <small style="left:144px">Copyrights © 2019 Marcus Trell. All rights reserved.</small>
  <small style="left:833px">Connect Us:</small>
  <div class="social" aria-label="Social links"><span></span><span></span><span></span><span></span></div>
</footer>

</body>
</html>
```